Tall Harbor Business Card

We are a Video Production and Video Equipment Rental company specialising in the supply of state of the art Video Technology and Services for the Live Entertainment, Television and Corporate Business Theatre markets. (in Sydney, Australia) www.tallharbor-media.example

Industry/Entity Type

Business

Contact Information for Business Card

name, position, email, website, address, logo
Example attached of the information we need - doesn't necessarily have to look the same

Font styles to use
Other font styles liked:
• Tall Harbor logo font is GOTHAM

Colors
ea1f27

Requirements
Nice to have
• either matt black or shiny black cards -
raised logo

```html
<!DOCTYPE html>
<html lang="en">
<head>
<meta charset="utf-8">
<title>Tall Harbor Business Card</title>
<link href="https://fonts.googleapis.com/css2?family=Questrial&display=swap" rel="stylesheet">
<style>
  :root {
    --page-bg: #e6e6e6;
    --card-black: #0d0d0d;
    --brand-red: #ea1f27;
    --text-white: #ffffff;
  }
  html, body {
    margin: 0;
    width: 1200px;
    height: 1000px;
    overflow: hidden;
    background: var(--page-bg);
    font-family: "Questrial", "Century Gothic", sans-serif;
  }
  .card {
    position: absolute;
    left: 92px;
    top: 186px;
    width: 1018px;
    height: 629px;
    background: var(--card-black);
    color: var(--text-white);
    overflow: hidden;
  }
  .card-shapes {
    position: absolute;
    inset: 0;
  }
  .brand-name {
    position: absolute;
    left: 153px;
    top: 68px;
    margin: 0;
    font-size: 40px;
    font-weight: 400;
    letter-spacing: 1px;
    text-transform: uppercase;
    color: var(--text-white);
  }
  .person {
    position: absolute;
    left: 81px;
    top: 303px;
  }
  .person-name {
    margin: 0;
    font-size: 40px;
    font-weight: 400;
    line-height: 1.1;
  }
  .person-role {
    margin: 4px 0 0 6px;
    font-size: 22px;
    letter-spacing: 3.5px;
  }
  .contact {
    position: absolute;
    text-align: center;
    font-size: 20px;
    line-height: 26px;
  }
  .contact .icon {
    height: 34px;
    display: flex;
    align-items: flex-end;
    justify-content: center;
    margin-bottom: 6px;
  }
  .contact svg {
    display: block;
    fill: none;
    stroke: var(--text-white);
    stroke-width: 2;
  }
  .contact p { margin: 0; }
  .contact-address { left: 537px; width: 400px; top: 134px; }
  .contact-office { left: 545px; width: 200px; top: 264px; }
  .contact-mobile { left: 728px; width: 200px; top: 264px; }
  .contact-email { left: 537px; width: 400px; top: 364px; }
  .contact-web { left: 537px; width: 400px; top: 462px; }
</style>
</head>
<body>
  <section class="card">
    <svg class="card-shapes" width="1018" height="629" viewBox="0 0 1018 629" aria-hidden="true">
      <defs>
        <linearGradient id="band-shade" x1="0" y1="0" x2="1018" y2="0" gradientUnits="userSpaceOnUse">
          <stop offset="0" stop-color="#3a3a3c"/>
          <stop offset="0.5" stop-color="#4e4e50"/>
          <stop offset="1" stop-color="#1c1c1d"/>
        </linearGradient>
        <linearGradient id="red-fade" x1="0" y1="0" x2="1018" y2="0" gradientUnits="userSpaceOnUse">
          <stop offset="0" stop-color="#ea1f27"/>
          <stop offset="0.55" stop-color="#ea1f27"/>
          <stop offset="1" stop-color="#3a0a0c"/>
        </linearGradient>
      </defs>
      <path class="top-band" d="M0 0 H1018 V102 H640 C590 102 585 155 540 155 H0 Z" fill="url(#band-shade)"/>
      <path class="top-rule" d="M0 155 H540 C585 155 590 102 640 102 H1018" fill="none" stroke="#ea1f27" stroke-width="3"/>
      <rect class="bottom-band" x="0" y="560" width="1018" height="69" fill="url(#band-shade)"/>
      <rect class="bottom-rule" x="0" y="557" width="1018" height="5" fill="url(#red-fade)"/>
    </svg>

    <h1 class="brand-name">Tall Harbor</h1>

    <div class="person">
      <p class="person-name">Your Name Here</p>
      <p class="person-role">Position</p>
    </div>

    <div class="contact contact-address">
      <div class="icon"><svg width="26" height="32" viewBox="0 0 26 32"><path d="M13 30 C6 20 2 15 2 11 A11 11 0 0 1 24 11 C24 15 20 20 13 30 Z"/></svg></div>
      <p>12 Wharf Lane, Kestrel Bay NSW 2999</p>
      <p>Australia</p>
    </div>

    <div class="contact contact-office">
      <div class="icon"><svg width="30" height="28" viewBox="0 0 30 28"><path d="M6 3 L11 8 L8 12 C10 17 13 20 17 22 L21 19 L26 24 L22 27 C12 25 4 16 3 7 Z" fill="#fff" stroke="none"/></svg></div>
      <p>+61 2 9400 1234</p>
    </div>

    <div class="contact contact-mobile">
      <div class="icon"><svg width="20" height="32" viewBox="0 0 20 32"><rect x="2" y="1" width="16" height="30" rx="3"/><line x1="2" y1="25" x2="18" y2="25"/></svg></div>
      <p>+61 4 1200 5678</p>
    </div>

    <div class="contact contact-email">
      <div class="icon"><svg width="36" height="24" viewBox="0 0 36 24"><rect x="1" y="1" width="34" height="22"/><path d="M1 1 L18 14 L35 1 M1 23 L14 11 M35 23 L22 11"/></svg></div>
      <p>hello@tallharbor-media.example</p>
    </div>

    <div class="contact contact-web">
      <div class="icon"><svg width="32" height="32" viewBox="0 0 32 32"><circle cx="16" cy="16" r="14"/><ellipse cx="16" cy="16" rx="6" ry="14"/><path d="M2 16 H30 M4 9 H28 M4 23 H28 M16 2 V30"/></svg></div>
      <p>www.tallharbor-media.example</p>
    </div>
  </section>
</body>
</html>
```